Electronic Security And Guard/Patrol Company Needs Half Page Advertisement

We need a half page ad designed for a 71 year old security company in Minnesota called PWTR (Pinnacle Watchtower Resources Incorporated). We are a full service security company providing electronic security solutions (Alarm Systems, Access Control Systems, Fire Systems, Video Surveillance Systems, etc) and Guard and Patrol services (Mobile Patrols, Alarm Response, Physical Guards, etc) for Residential and Commercial customers. We would like a design that grabs attention simply and portrays high tech Residential & Commercial security systems. We would like our logo (attached), website (www.pwtr-example.net), and phone number (555-314-2708) included. Also possibly like to communicate we have been in business in Since 1946. The particular add is for a half page add in a magazine and should be 7" x 4.75", and must be able to be resized for future half page ads. For additional information, please see our website: www.pwtr-example.net

Target Market(s)

Residential Homeowners & Business Owners

Industry/Entity Type

Security

Colors

Designer to choose colors to be used in the design.

Requirements
Must have
• Logo
• Phone Number (555-467-1193)
• Website (www.pwtr-example.net)
Nice to have
• Maybe Small Text Of Basic Overview of Services Provided: Security Systems, Video Surveillance, Access Control, Fire, Monitoring, Guard & Patrol Services

```html
<!DOCTYPE html>
<html lang="en">
<head>
<meta charset="utf-8">
<title>PWTR – Half Page Advertisement</title>
<link href="https://fonts.googleapis.com/css2?family=Open+Sans:wght@400;600;700&family=Roboto+Condensed:wght@700&display=swap" rel="stylesheet">
<style>
  :root {
    --page-bg: #e6ebef;
    --card-top: #f3f4f5;
    --card-bottom: #e9ebed;
    --navy: #1b5a86;
    --band: #156694;
    --sky: #1d9ad8;
    --ink: #2b2b2b;
    --white: #ffffff;
    --hex-fill: #eef2f5;
    --gold-light: #ecd07a;
    --gold-dark: #b08a34;
  }
  * { box-sizing: border-box; margin: 0; padding: 0; }
  html, body { width: 1020px; height: 1200px; overflow: hidden; }
  body { background: var(--page-bg); font-family: "Open Sans", Arial, sans-serif; position: relative; }

  .ad {
    position: absolute; left: 102px; top: 5px; width: 816px; height: 1190px;
    background: linear-gradient(var(--card-top), var(--card-bottom));
    overflow: hidden; box-shadow: 0 2px 10px rgba(0,0,0,.15);
  }

  .brand { position: absolute; left: 290px; top: 18px; text-align: center; width: 240px; }
  .brand-name { font-family: "Roboto Condensed", Arial, sans-serif; font-weight: 700; font-size: 58px; line-height: 1; color: var(--ink); letter-spacing: 2px; }
  .brand-tagline { font-size: 15px; color: var(--ink); margin-top: 6px; }

  .since { position: absolute; right: 30px; top: 22px; text-align: left; }
  .since-title { font-size: 29px; font-weight: 700; color: var(--navy); }
  .since-web { font-size: 22px; color: var(--sky); display: flex; align-items: center; gap: 8px; margin-top: 2px; }

  .hero { position: absolute; left: 0; top: 100px; width: 816px; height: 540px; }

  .headline {
    position: absolute; left: 0; width: 100%; top: 648px; text-align: center;
    font-family: "Roboto Condensed", Arial, sans-serif; font-weight: 700; font-size: 32px;
    line-height: 42px; color: var(--navy);
  }

  .services { position: absolute; left: 0; top: 736px; width: 100%; height: 296px; background: var(--band); }
  .services-title {
    position: absolute; left: 282px; top: 16px; width: 265px; height: 48px; border-radius: 8px;
    background: var(--sky); color: var(--white); font-size: 27px; text-align: center; line-height: 48px;
  }
  .service { position: absolute; top: 92px; width: 200px; margin-left: -100px; text-align: center; color: var(--white); font-size: 21px; line-height: 30px; }
  .service svg { display: block; margin: 0 auto 14px; }

  .guard { position: absolute; left: 35px; top: 1042px; }
  .guard-title { font-size: 21px; font-weight: 700; color: var(--navy); margin-bottom: 6px; }
  .guard-list { list-style: none; font-size: 21px; color: var(--ink); line-height: 34px; }
  .guard-list li { display: flex; align-items: center; gap: 12px; }

  .address { position: absolute; left: 505px; top: 1050px; font-size: 21px; line-height: 28px; color: var(--navy); display: flex; gap: 12px; }
  .call { position: absolute; right: 36px; top: 1126px; font-family: "Roboto Condensed", Arial, sans-serif; font-weight: 700; font-size: 45px; line-height: 56px; color: var(--navy); }
  .base-stripe { position: absolute; left: 0; bottom: 0; width: 100%; height: 8px; background: var(--sky); }
</style>
</head>
<body>
<main class="ad">
  <header>
    <div class="brand">
      <div class="brand-name">PWTR</div>
      <div class="brand-tagline">Safety &amp; Security Solutions</div>
    </div>
    <div class="since">
      <div class="since-title">in Since 1946</div>
      <div class="since-web">
        <svg width="18" height="18" viewBox="0 0 20 20"><circle cx="10" cy="10" r="8.5" fill="none" stroke="currentColor" stroke-width="1.8"/><path d="M1.5 10h17M10 1.5c-4 4.5-4 12.5 0 17M10 1.5c4 4.5 4 12.5 0 17" fill="none" stroke="currentColor" stroke-width="1.5"/></svg>
        www.pwtr-example.net
      </div>
    </div>
  </header>

  <svg class="hero" viewBox="0 0 816 540">
    <defs>
      <linearGradient id="photoTone" x1="0" y1="0" x2="1" y2="1">
        <stop offset="0" stop-color="#5d7286"/>
        <stop offset=".45" stop-color="#b9c6d2"/>
        <stop offset="1" stop-color="#dfe6ec"/>
      </linearGradient>
      <radialGradient id="medalTone" cx=".45" cy=".4" r=".65">
        <stop offset="0" stop-color="var(--gold-light)"/>
        <stop offset="1" stop-color="var(--gold-dark)"/>
      </radialGradient>
    </defs>
    <path d="M0 30 Q408 -25 816 62 L816 78 Q408 -5 0 46 Z" fill="var(--sky)"/>
    <path role="img" aria-label="Security operator monitoring camera feeds at a control room workstation" d="M0 52 Q408 2 816 84 L816 460 Q408 530 0 460 Z" fill="url(#photoTone)"/>
    <path d="M0 460 Q408 530 816 460 L816 478 Q408 550 0 478 Z" fill="var(--white)"/>
    <path d="M0 474 Q408 546 816 474 L816 490 Q408 562 0 490 Z" fill="var(--sky)"/>
    <circle role="img" aria-label="Gold anniversary medal celebrating 71 years, 1946 to 2016" cx="707" cy="405" r="88" fill="url(#medalTone)"/>
  </svg>

  <h1 class="headline">We are a full Service Security company providing<br>Electronic Security Solutions</h1>

  <section class="services">
    <div class="services-title">OUR SERVICES</div>
    <div class="service" style="left:96px">
      <svg width="120" height="126" viewBox="0 0 120 126"><polygon points="60,2 115,32 115,94 60,124 5,94 5,32" fill="var(--hex-fill)"/><path d="M60 38c8 12 20 20 20 36a20 20 0 0 1-40 0c0-8 4-14 8-18 0 6 3 10 6 10-2-10 0-20 6-28z" fill="var(--band)"/></svg>
      Fire Systems
    </div>
    <div class="service" style="left:288px">
      <svg width="120" height="126" viewBox="0 0 120 126"><polygon points="60,2 115,32 115,94 60,124 5,94 5,32" fill="var(--hex-fill)"/><path d="M60 40c-10 0-16 8-16 18v14l-6 8h44l-6-8V58c0-10-6-18-16-18z" fill="var(--band)"/><circle cx="60" cy="85" r="5" fill="var(--band)"/><path d="M36 44a30 30 0 0 0-8 20M84 44a30 30 0 0 1 8 20M30 40a38 38 0 0 0-9 26M90 40a38 38 0 0 1 9 26" fill="none" stroke="var(--band)" stroke-width="3"/></svg>
      Alarm Systems
    </div>
    <div class="service" style="left:496px">
      <svg width="120" height="126" viewBox="0 0 120 126"><polygon points="60,2 115,32 115,94 60,124 5,94 5,32" fill="var(--hex-fill)"/><rect x="38" y="36" width="36" height="52" rx="3" fill="var(--band)"/><rect x="43" y="41" width="26" height="10" fill="var(--hex-fill)"/><g fill="var(--hex-fill)"><rect x="44" y="56" width="6" height="5"/><rect x="53" y="56" width="6" height="5"/><rect x="62" y="56" width="6" height="5"/><rect x="44" y="65" width="6" height="5"/><rect x="53" y="65" width="6" height="5"/><rect x="62" y="65" width="6" height="5"/><rect x="44" y="74" width="6" height="5"/><rect x="53" y="74" width="6" height="5"/></g><rect x="70" y="66" width="16" height="24" rx="3" fill="var(--band)" stroke="var(--hex-fill)" stroke-width="2"/></svg>
      Access<br>Control Systems
    </div>
    <div class="service" style="left:691px">
      <svg width="120" height="126" viewBox="0 0 120 126"><polygon points="60,2 115,32 115,94 60,124 5,94 5,32" fill="var(--hex-fill)"/><rect x="32" y="42" width="56" height="10" rx="2" fill="var(--band)"/><path d="M36 54h48a24 24 0 0 1-48 0z" fill="var(--band)"/><circle cx="60" cy="64" r="8" fill="var(--hex-fill)"/><circle cx="60" cy="64" r="4" fill="var(--band)"/></svg>
      Video Surveillance<br>Systems
    </div>
  </section>

  <section class="guard">
    <h2 class="guard-title">GUARD AND PATROL SERVICES</h2>
    <ul class="guard-list">
      <li><svg width="16" height="14" viewBox="0 0 16 14"><path d="M1 7l5 5L15 1" fill="none" stroke="var(--sky)" stroke-width="2.5"/></svg>Mobile Patrols</li>
      <li><svg width="16" height="14" viewBox="0 0 16 14"><path d="M1 7l5 5L15 1" fill="none" stroke="var(--sky)" stroke-width="2.5"/></svg>Alarm Response</li>
      <li><svg width="16" height="14" viewBox="0 0 16 14"><path d="M1 7l5 5L15 1" fill="none" stroke="var(--sky)" stroke-width="2.5"/></svg>Physical Guards</li>
    </ul>
  </section>

  <div class="address">
    <svg width="14" height="20" viewBox="0 0 14 20" style="margin-top:4px"><path d="M7 0a7 7 0 0 1 7 7c0 5-7 13-7 13S0 12 0 7a7 7 0 0 1 7-7z" fill="var(--navy)"/><circle cx="7" cy="7" r="2.6" fill="var(--white)"/></svg>
    <div>4820 Ridgecrest Road<br>Minneapolis, MN 55499</div>
  </div>

  <div class="call">Call us: 555-467-1193</div>
  <div class="base-stripe"></div>
</main>
</body>
</html>
```